New Hotel Showcase Website

We plan to launch a website called www.brindlestays.net which showcases the world’s best new hotels. We want a mock up for 2 pages: the homepage (page 1) and the individual hotel page (page 2). We are looking for a design which combines simplicity while highlighting images/features of the hotel. Because the theme of the site is new hotels it is important that the design somehow emphasizes the age of each hotel listed – both on the homepage and then on the individual hotel page.

NOTE: WE WANT A CREATIVE, NEW APPROACH TO DISPLAYING HOTELS. NOT JUST A COPY OF CURRENT HOTEL WEBSITES.

The design should consider unique and creative ways of helping users to navigate the homepage (page 1) based on the age, location or style of the hotel they are interested in. The individual hotel page(page 2) can be more standard by clearly setting out hotel photos, feature lists, reviews, contact details and potential discounts. There is no booking system needed as this is not a hotel booking website.

The design should ideally be compatible with a content management system such as Page Loom. In terms of reference materials we like sites similar to:

http://www.velmarquay.net
http://www.corvidandpine.net
http://www.tessarooms.net
http://www.quillbeds.net

These sites are designed far more simply than large booking sites such as www.roamvix.net, www.bunkfold.net or even wander ledger. However, we are not looking for a copy of the above. We are looking for a design that presents hotels in a novel way and would be seen by the industry as a unique way of displaying new hotels.
Updates

Dear Designers - we have received quite a few entries already. Thank you. However, none of the designs submitted have responded to our brief. They are all copies or derivatives of current hotel websites which is not what we are looking for. We want (a) a new and creative approach to a hotel website and (b) one which creatively uses the age of the hotel (ie. 1 month old, 6 months old etc).

It will require creative thinking and new ideas. We wanted to challenge designers to come up with something new. Thanks.

```html
<!DOCTYPE html>
<html lang="en">
<head>
<meta charset="utf-8">
<title>Brindlestays – New hotels, hand selected</title>
<link rel="stylesheet" href="https://fonts.googleapis.com/css2?family=Josefin+Sans:wght@300;400&family=Arimo:wght@400;700&display=swap">
<style>
  :root {
    --navy-deep: #02022a;
    --band: rgba(14, 22, 90, 0.82);
    --accent-blue: #0a8fe0;
    --lime: #8cd11e;
    --white: #ffffff;
    --nav-text: #0d1f4a;
    --nav-active: #7cc3ee;
    --title: #132a63;
    --info-tile: #08084e;
    --footer-text: #e9ecf5;
  }
  * { box-sizing: border-box; margin: 0; padding: 0; }
  html, body { width: 1200px; height: 962px; overflow: hidden; background: var(--white); }
  body { position: relative; font-family: "Arimo", Arial, sans-serif; }

  .hero {
    position: absolute; left: 0; top: 0; width: 1200px; height: 536px;
    background:
      radial-gradient(ellipse 260px 90px at 130px 270px, rgba(226,178,120,0.55), transparent 75%),
      radial-gradient(ellipse 420px 260px at 1080px 260px, rgba(30,34,60,0.6), transparent 72%),
      radial-gradient(ellipse 700px 90px at 560px 470px, rgba(214,160,96,0.35), transparent 75%),
      radial-gradient(ellipse 500px 180px at 640px 330px, rgba(20,90,200,0.55), transparent 75%),
      linear-gradient(180deg, #8ab8dc 0%, #5b97cc 18%, #2f74bd 34%, #1c58a8 55%, #173f86 75%, #3a4668 100%);
  }
  .site-header {
    position: absolute; left: 0; top: 0; width: 1200px; height: 62px;
    background: linear-gradient(180deg, rgba(255,255,255,0.8), rgba(214,232,246,0.6));
    border-bottom: 1px solid rgba(255,255,255,0.75);
  }
  .brand { position: absolute; left: 187px; top: 15px; display: flex; align-items: center; gap: 15px; }
  .brand-mark { width: 32px; height: 32px; background: var(--accent-blue); }
  .brand-name { font-size: 36px; font-weight: 400; color: var(--white); letter-spacing: -0.5px; line-height: 1; }
  .main-nav { position: absolute; left: 574px; top: 0; display: flex; height: 62px; }
  .main-nav a {
    display: block; height: 62px; line-height: 78px; padding: 0 10px;
    font-size: 12.5px; color: var(--nav-text); text-decoration: none;
  }
  .main-nav a.is-active { background: var(--nav-active); color: var(--white); width: 47px; padding: 0; text-align: center; margin-right: 2px; }

  .hero-headline {
    position: absolute; left: 232px; top: 132px;
    font-family: "Josefin Sans", "Century Gothic", sans-serif; font-weight: 300;
    font-size: 33px; line-height: 42px; color: var(--white); letter-spacing: 0.6px;
  }
  .hero-headline span { display: block; }
  .signup { position: absolute; left: 234px; top: 302px; }
  .signup h2 {
    font-family: "Josefin Sans", "Century Gothic", sans-serif; font-weight: 400;
    font-size: 17px; line-height: 20px; color: var(--white); margin-bottom: 16px;
  }
  .signup .field {
    width: 220px; height: 30px; background: var(--white); margin-bottom: 7px;
    font-size: 11px; color: var(--nav-text); padding: 14px 8px 0;
  }
  .signup .btn {
    width: 101px; height: 30px; background: var(--accent-blue); color: var(--white);
    font-size: 12.5px; text-align: center; line-height: 30px; margin-top: 9px;
  }
  .slider-dots { position: absolute; left: 958px; top: 433px; display: flex; gap: 5px; }
  .slider-dots i { display: block; width: 10px; height: 10px; border: 1px solid var(--white); }
  .slider-dots i.is-current { background: var(--accent-blue); }

  .perks { position: absolute; left: 0; top: 471px; width: 1200px; height: 65px; background: var(--band); }
  .perk-icon { position: absolute; top: 15px; }
  .perk-text {
    position: absolute; top: 17px; font-size: 11px; line-height: 16px;
    color: var(--white); letter-spacing: 0.4px;
  }

  .gallery-title { position: absolute; left: 239px; top: 598px; font-size: 21px; line-height: 26px; color: var(--title); font-weight: 400; }
  .tile { position: absolute; width: 164px; height: 74px; }
  .tile-info { background: var(--info-tile); color: var(--white); text-align: center; padding-top: 15px; }
  .tile-info h3 { font-size: 11px; line-height: 13px; font-weight: 400; margin-bottom: 3px; }
  .tile-info p { font-size: 9.5px; line-height: 13px; margin-bottom: 3px; }
  .tile-info a { font-size: 9.5px; line-height: 13px; color: var(--lime); text-decoration: none; }
  .tile-info svg { position: absolute; left: 112px; top: 52px; }

  .site-footer { position: absolute; left: 0; top: 908px; width: 1200px; height: 54px; background: var(--navy-deep); }
  .copyright { position: absolute; left: 187px; top: 20px; font-size: 11px; line-height: 13px; color: var(--footer-text); }
  .copyright em { font-style: normal; color: var(--lime); }
  .social { position: absolute; left: 860px; top: 13px; display: flex; gap: 2px; }
  .social span { display: block; width: 29px; height: 29px; border-radius: 2px; }
</style>
</head>
<body>
  <section class="hero" role="img" aria-label="Evening photo of an infinity pool terrace with lounge chairs, a floor lamp and candles overlooking a calm sea bay"></section>

  <header class="site-header">
    <div class="brand"><span class="brand-mark"></span><span class="brand-name">BRINDLESTAYS</span></div>
    <nav class="main-nav">
      <a class="is-active" href="#">Home</a>
      <a href="#">About Us</a>
      <a href="#">Hotel Photos</a>
      <a href="#">Feature Lists</a>
      <a href="#">Reviews</a>
      <a href="#">Contact&nbsp; Us</a>
    </nav>
  </header>

  <h1 class="hero-headline">
    <span>New hotels.</span>
    <span>Hand selected.</span>
    <span>Exclusive opening prices.</span>
  </h1>

  <form class="signup">
    <h2>Beta sign up</h2>
    <div class="field">Name...</div>
    <div class="field">Email Address...</div>
    <div class="btn">Membership</div>
  </form>

  <div class="slider-dots"><i></i><i></i><i></i><i class="is-current"></i></div>

  <section class="perks">
    <svg class="perk-icon" style="left:187px" width="34" height="32" viewBox="0 0 34 32" fill="none" stroke="#8cd11e" stroke-width="2.5" stroke-linecap="round">
      <path d="M5 18 L31 7"/><path d="M13 14 L9 5"/><path d="M19 12 L23 23"/><path d="M2 30 H32"/>
    </svg>
    <p class="perk-text" style="left:235px">Enjoy exclusive prices as hotels<br>open their doors</p>

    <svg class="perk-icon" style="left:492px" width="36" height="34" viewBox="0 0 36 34" fill="none" stroke="#8cd11e" stroke-width="2">
      <path d="M6 14 H18 L12 23 Z"/><path d="M12 23 V31"/><path d="M20 4 L26 16"/><circle cx="28" cy="24" r="4"/><path d="M2 32 H34"/>
    </svg>
    <p class="perk-text" style="left:542px">We select only the most luxurious,<br>designer and boutique hotels</p>

    <svg class="perk-icon" style="left:821px" width="32" height="28" viewBox="0 0 32 28" fill="none" stroke="#8cd11e" stroke-width="2.5">
      <rect x="2" y="5" width="28" height="20"/><path d="M6 21 L13 13 L18 18 L22 14 L27 21 Z" fill="#8cd11e"/>
    </svg>
    <p class="perk-text" style="left:867px">Never stay at tired, overpriced<br>hotels again</p>
  </section>

  <h2 class="gallery-title">Hotels Detail &amp; Location</h2>

  <div class="tile" style="left:517px;top:573px;background:linear-gradient(180deg,#2a8ac0 0%,#1a5a86 35%,#3a6a86 60%,#8a5a30 100%)" role="img" aria-label="Underwater hotel suite beneath an aquarium ceiling"></div>
  <div class="tile" style="left:683px;top:573px;background:linear-gradient(180deg,#3448b8 0%,#7a92e0 40%,#3a3a40 60%,#2a8ad0 80%,#1a5aa0 100%)" role="img" aria-label="Resort villas around a blue infinity pool"></div>

  <div class="tile" style="left:187px;top:649px;background:linear-gradient(180deg,#0c0c10 0%,#1e1a14 45%,#6a5230 70%,#201a12 100%)" role="img" aria-label="Waterfront hotel towers lit at night"></div>
  <div class="tile" style="left:352px;top:649px;background:linear-gradient(180deg,#e6eef4 0%,#8eb0c6 40%,#6a8696 70%,#d6dce0 100%)" role="img" aria-label="Rooftop terrace with parasols over a city"></div>
  <div class="tile" style="left:517px;top:649px;background:linear-gradient(180deg,#c2a6b4 0%,#8a7090 40%,#5a4a68 70%,#2e2840 100%)" role="img" aria-label="Riverside temple view at dusk"></div>
  <div class="tile tile-info" style="left:683px;top:649px">
    <h3>LOREM IPSUM</h3>
    <p>Age : 7 year &nbsp;|&nbsp; Location : Vivamus</p>
    <a href="#">View More</a>
    <svg width="14" height="16" viewBox="0 0 14 16" fill="#fff" stroke="#08084e" stroke-width="0.8"><path d="M4 1 V9 L2 7.5 L1 8.5 L5 15 H12 L13 9 L12 7 H9 V5 H7 V4 H6 V1 Z"/></svg>
  </div>
  <div class="tile" style="left:848px;top:649px;background:linear-gradient(90deg,#1a2028 0%,#8a7020 35%,#c8a82a 50%,#4a4030 75%,#1e2228 100%)" role="img" aria-label="Illuminated gold hotel tower at night"></div>

  <div class="tile" style="left:187px;top:723px;background:linear-gradient(180deg,#b4cee4 0%,#eef2f4 50%,#a8d0dc 75%,#86b8c8 100%)" role="img" aria-label="White beach pavilion by the sea"></div>
  <div class="tile" style="left:352px;top:723px;background:linear-gradient(180deg,#3a3048 0%,#8a4a3a 40%,#c0683a 65%,#4a3030 100%)" role="img" aria-label="Pier hotel at sunset"></div>
  <div class="tile" style="left:517px;top:723px;background:linear-gradient(180deg,#4a6ac0 0%,#2a46a0 40%,#1e2a60 70%,#8a6a30 100%)" role="img" aria-label="Curved glass hotel at twilight"></div>
  <div class="tile" style="left:683px;top:723px;background:linear-gradient(180deg,#a2c6e6 0%,#d6dee4 45%,#9aaab6 70%,#7aa2c0 100%)" role="img" aria-label="Dome shaped floating hotel"></div>
  <div class="tile" style="left:848px;top:723px;background:linear-gradient(180deg,#7a8c9a 0%,#5a6470 45%,#3a3e44 70%,#24262a 100%)" role="img" aria-label="Futuristic disc shaped building"></div>

  <div class="tile" style="left:352px;top:798px;background:linear-gradient(180deg,#2a76d6 0%,#6aa6e6 35%,#dce6ee 60%,#2a6aa6 100%)" role="img" aria-label="Seaside white hotel under blue sky"></div>
  <div class="tile" style="left:517px;top:798px;background:linear-gradient(180deg,#2a2838 0%,#6a5e3a 40%,#9a8a50 65%,#30281a 100%)" role="img" aria-label="Classic hotel facade lit at evening"></div>

  <footer class="site-footer">
    <p class="copyright">Copyright © 2013 <em>BRINDLESTAY</em> . All Rights Reserved.</p>
    <div class="social" aria-label="Social links">
      <span style="background:#3a5a9a"></span>
      <span style="background:#3aa8d8"></span>
      <span style="background:#2a7ab8"></span>
      <span style="background:#d04a3a"></span>
      <span style="background:#b8b070"></span>
    </div>
  </footer>
</body>
</html>
```